Financial Services Business Card Design

We are a financial services company Based in London, offering Short term Funding Solutions for companies, raising anywhere between £20,000 and £25million pounds.

The Card must have a professional look as it is going to be handed out to professionals I.E Solicitors, Accountants, Company directors and Business owners.

See Attached our company Logo

Industry/Entity Type

Business

Contact Information for Business Card

Brett Kolvane
Suite 41
R T House
Hazelbrook Lane
Watford
WD17 4QL

```html
<!DOCTYPE html>
<html lang="en">
<head>
<meta charset="utf-8">
<title>Brightwell Finance Hub – Business Card</title>
<link rel="stylesheet" href="https://fonts.googleapis.com/css2?family=Lato:wght@400;700;900&display=swap">
<style>
  :root {
    --backdrop: #2e2e2e;
    --card: #f7f8f8;
    --brand-blue: #1e63ad;
    --brand-green: #3aa33a;
    --ink: #2a2a2a;
    --faint-blue: #c9d8ea;
  }
  * { margin: 0; padding: 0; box-sizing: border-box; }
  html, body {
    width: 1200px; height: 997px; overflow: hidden;
    background: var(--backdrop);
    font-family: "Lato", Arial, sans-serif;
  }
  .stage { position: relative; width: 1200px; height: 997px; }
  .card {
    position: absolute; width: 620px; height: 354px;
    background: var(--card); overflow: hidden;
    box-shadow: 0 12px 30px rgba(0,0,0,.45);
  }
  .card-back { left: 70px; top: 80px; }
  .card-front { left: 510px; top: 470px; }
  .bands { position: absolute; inset: 0; width: 620px; height: 354px; }
  .band-green { fill: var(--brand-green); }
  .band-blue { fill: var(--brand-blue); }

  .back-mark {
    position: absolute; left: 0; right: 0; top: 140px;
    text-align: center; font-weight: 900; font-size: 48px;
    letter-spacing: 2px; color: var(--faint-blue); text-transform: uppercase;
  }

  .holder { position: absolute; left: 66px; top: 78px; }
  .holder-name {
    color: var(--brand-blue); font-weight: 700; font-size: 25px;
    letter-spacing: 1px; text-transform: uppercase;
  }
  .holder-role { color: var(--ink); font-size: 15px; margin-top: 2px; }

  .brand { position: absolute; right: 34px; top: 168px; display: flex; align-items: center; gap: 10px; }
  .brand-dot { width: 22px; height: 22px; border-radius: 50%; background: var(--brand-blue); }
  .brand-name {
    color: var(--brand-blue); font-weight: 900; font-size: 31px;
    letter-spacing: 1px; text-transform: uppercase; line-height: 1.05;
  }

  .contact-tab {
    position: absolute; left: 0; top: 222px; width: 40px; height: 108px;
    background: var(--brand-blue); border-radius: 0 14px 14px 0;
  }
  .contact-tab svg { position: absolute; left: 11px; width: 18px; height: 18px; fill: none; stroke: #fff; stroke-width: 1.8; }
  .contact-list { position: absolute; left: 60px; top: 222px; list-style: none; color: var(--ink); font-size: 17px; line-height: 1.25; }
  .contact-list li { margin-bottom: 10px; }
  .contact-list .address { margin-bottom: 0; }
</style>
</head>
<body>
<main class="stage">
  <section class="card card-back" aria-label="Card back">
    <p class="back-mark">Brightwell Finance Hub</p>
    <svg class="bands" viewBox="0 0 620 354" aria-hidden="true">
      <polygon class="band-green" points="0,340 440,340 452,326 620,326 620,354 0,354"/>
      <polygon class="band-blue" points="470,300 620,300 620,326 452,326"/>
    </svg>
  </section>

  <section class="card card-front" aria-label="Card front">
    <div class="holder">
      <p class="holder-name">Brett Kolvane</p>
      <p class="holder-role">Owner</p>
    </div>

    <div class="brand">
      <span class="brand-dot"></span>
      <span class="brand-name">Brightwell<br>Finance Hub</span>
    </div>

    <div class="contact-tab">
      <svg style="top:12px" viewBox="0 0 18 18" aria-hidden="true"><rect x="5" y="1.5" width="8" height="15" rx="1.5"/></svg>
      <svg style="top:45px" viewBox="0 0 18 18" aria-hidden="true"><rect x="2" y="4" width="14" height="10" rx="1"/><polyline points="2,4 9,10 16,4"/></svg>
      <svg style="top:78px" viewBox="0 0 18 18" aria-hidden="true"><path d="M9 16s-5-5-5-9a5 5 0 0 1 10 0c0 4-5 9-5 9z"/><circle cx="9" cy="7" r="1.8"/></svg>
    </div>

    <ul class="contact-list">
      <li>613-555-0172</li>
      <li>info@brightwellfh.com</li>
      <li class="address">Suite 41 R T House Hazelbrook Lane<br>Watford WD17 4QL</li>
    </ul>

    <svg class="bands" viewBox="0 0 620 354" aria-hidden="true">
      <polygon class="band-green" points="0,340 440,340 452,326 620,326 620,354 0,354"/>
      <polygon class="band-blue" points="470,300 620,300 620,326 452,326"/>
    </svg>
  </section>
</main>
</body>
</html>
```